Need Exciting Podcast Cover Art Design for New Show!

We need a podcast art design for our new show. It is called "Plan Craft Thrive a Label" and we've interviewed hundreds of proven online entrepreneurs and experts and asked them to share their best advice for starting an e-commerce product-based brand. I don't have a color palette however, I like Blue (but I'm open to your suggestion). I want a podcast cover art that stands out, jumps out when people are browsing.

Target Market(s)

People who have a product idea and want to sell it online directly to the consumer

Font styles to use
Sans Serif

Requirements
Must have
• It should have the name: The Plan Craft Thrive a Label Show and the most important words in the title/they should stand out are Plan Craft Thrive
Nice to have
• I want something simple yet I want it to pop out. For instance, if you use blue, add a hint of color to make it pop.

```html
<!DOCTYPE html>
<html lang="en">
<head>
<meta charset="utf-8">
<title>The Plan Craft Thrive a Label Show — Podcast Cover</title>
<link rel="stylesheet" href="https://fonts.googleapis.com/css2?family=Archivo:wdth,wght@62..125,800..900&display=swap">
<style>
  :root {
    --blue-deep: #0028ff;
    --blue-mid: #0a78ff;
    --blue-sky: #00bcff;
    --accent-green: #22ff00;
    --title-white: #ffffff;
    --shadow-navy: rgba(0, 18, 140, 0.55);
  }
  html, body {
    margin: 0;
    padding: 0;
    width: 1200px;
    height: 1200px;
    overflow: hidden;
    background: var(--blue-deep);
  }
  .cover {
    display: block;
    width: 1200px;
    height: 1200px;
  }
  .cover__title {
    font-family: "Archivo", "Arial Narrow", sans-serif;
    font-stretch: 75%;
    font-weight: 900;
    fill: var(--title-white);
    filter: drop-shadow(0 0 18px var(--shadow-navy));
  }
  .cover__title--small { font-size: 74px; }
  .cover__title--main { font-size: 205px; }
  .cover__title--tag { font-size: 104px; }
  .growth-bar, .growth-arrow { fill: var(--accent-green); }
  .climbers { fill: rgba(255, 255, 255, 0.28); }
</style>
</head>
<body>
<svg class="cover" viewBox="0 0 1200 1200" xmlns="http://www.w3.org/2000/svg">
  <defs>
    <linearGradient id="sky" x1="0.3" y1="0" x2="0.75" y2="1">
      <stop offset="0" stop-color="var(--blue-deep)"/>
      <stop offset="0.5" stop-color="var(--blue-mid)"/>
      <stop offset="0.85" stop-color="var(--blue-sky)"/>
    </linearGradient>
  </defs>

  <rect class="backdrop" width="1200" height="1200" fill="url(#sky)"/>

  <polygon class="growth-arrow" points="806,416 836,467 1007,369 1040,425 1113,261 935,242 977,318"/>
  <polygon class="growth-bar" points="40,858 68,910 351,748 322,696"/>

  <rect class="climbers" role="img" aria-label="Two stick figures climbing the rising bar together"
        x="66" y="640" width="190" height="218" rx="14"/>

  <g class="cover__heading">
    <text class="cover__title cover__title--small" transform="translate(360,328) rotate(-30)"
          textLength="126" lengthAdjust="spacingAndGlyphs">THE</text>
    <text class="cover__title cover__title--main" transform="translate(283,571) rotate(-30)"
          textLength="487" lengthAdjust="spacingAndGlyphs">PLAN</text>
    <text class="cover__title cover__title--main" transform="translate(405,772) rotate(-30)"
          textLength="382" lengthAdjust="spacingAndGlyphs">CRAFT</text>
    <text class="cover__title cover__title--main" transform="translate(484,913) rotate(-30)"
          textLength="487" lengthAdjust="spacingAndGlyphs">THRIVE</text>
    <text class="cover__title cover__title--tag" transform="translate(551,1025) rotate(-30)"
          textLength="486" lengthAdjust="spacingAndGlyphs">A LABEL SHOW</text>
  </g>
</svg>
</body>
</html>
```